Tovrin SnapStand

Hi There,

I am looking to rebuild my company website.

Here are the development specs for my new site!:

1) I've designed a layout for my site and am looking for someone to incorporate the graphics into a word press template. Enclosed is a screen grab of the look and feel (all of the images / graphic working files are available).

2) The site needs to be built on a wordpress platform so that I can regularly edit the site content and make changes / updates

4) The web content (text) has not been finalized and is still being created. For now, I would really like to get the site developed (from a functionality standpoint) and provide text for each page as we finalize the site development.

I'm really excited to get my site redeveloped and launched!

Industry/Entity Type

It Company

Requirements
Must have
• Home Page to have rotating images

```html
<!DOCTYPE html>
<html lang="en">
<head>
<meta charset="utf-8">
<title>Tovrin SnapStand</title>
<link href="https://fonts.googleapis.com/css2?family=Oswald:wght@400&family=Roboto+Slab:wght@700&family=Ubuntu:ital,wght@0,400;0,500;0,700;1,500;1,700&display=swap" rel="stylesheet">
<style>
:root{
  --ink:#222;
  --grey:#5f5f61;
  --band:#1b1c1f;
  --panel:#232427;
  --blue:#2f5fc4;
  --blue-title:#3f78de;
  --tile:#5f7dc0;
  --magenta:#a01f5c;
  --card:#ebebec;
  --line:#cfcfd2;
  --white:#fff;
}
*{box-sizing:border-box;margin:0;padding:0}
html,body{width:947px;height:1200px;overflow:hidden}
body{position:relative;background:var(--white);font-family:"Ubuntu",sans-serif;color:var(--ink)}
.abs{position:absolute}

.brand{left:29px;top:40px;display:flex;align-items:center;gap:10px}
.brand-dot{width:46px;height:46px;border-radius:50%;background:#4a72b8}
.brand-name{font-weight:700;font-size:31px;color:var(--grey);letter-spacing:-0.5px}

.nav{left:328px;top:105px;height:42px;display:flex;background:linear-gradient(#4a4a4c,#1e1e20);border:1px solid #111}
.nav a{display:flex;align-items:center;justify-content:center;color:#fff;text-decoration:none;font-size:13px;font-weight:500;border-right:1px solid #0e0e0f;border-left:1px solid #555}
.nav a:nth-child(1){width:80px}.nav a:nth-child(2){width:94px}.nav a:nth-child(3){width:94px}
.nav a:nth-child(4){width:131px}.nav a:nth-child(5){width:76px}.nav a:nth-child(6){width:97px}

.band{left:0;top:147px;width:947px;height:311px;background:var(--band)}
.slider{left:44px;top:190px;width:852px;height:328px;background:var(--panel);box-shadow:0 8px 14px rgba(0,0,0,.35)}
.slide-photo{left:18px;top:17px;width:498px;height:279px;background:linear-gradient(135deg,#f4f4f4 0%,#9a8a80 40%,#3a3030 70%,#e8e8e8 100%)}
.slide-title{left:534px;top:16px;font-family:"Oswald",sans-serif;font-weight:400;font-size:34px;color:var(--blue-title);letter-spacing:.5px}
.slide-text{left:536px;top:67px;width:306px;font-size:12.4px;line-height:20.6px;color:#fff}
.know-more{left:681px;top:260px;width:150px;height:37px;background:linear-gradient(#3f6fc9,#2a50a3);display:flex;align-items:center;justify-content:center;gap:9px;color:#fff;font-family:"Roboto Slab",serif;font-weight:700;font-size:13.5px;letter-spacing:.3px}
.dots{left:224px;top:311px;display:flex;gap:6px}
.dots i{width:8px;height:8px;border-radius:50%;background:#bbb}
.dots i:first-child{background:#c21f1f}

.welcome{left:49px;top:540px;width:282px}
.welcome h1{font-size:18.5px;font-style:italic;font-weight:700;color:var(--ink);white-space:nowrap}
.welcome h1 span{color:var(--blue)}
.welcome p{margin-top:12px;font-size:10.6px;line-height:15.5px}
.welcome h2{margin-top:12px;font-size:13px;font-style:italic;font-weight:700;color:var(--magenta)}
.welcome .events{margin-top:12px;font-size:13.4px;font-style:italic;font-weight:500;line-height:20.8px;color:#3a3a3a}

.media-box{left:355px;top:539px;width:542px;height:294px;border:1px solid #bbb;padding:6px}
.media-inner{width:100%;height:100%;background:var(--panel);position:relative}
.media-tile{top:32px;width:227px;height:161px;background:var(--tile);display:flex;align-items:center;justify-content:center}
.media-cap{top:206px;width:227px;text-align:center;color:#fff;font-size:19px;font-weight:500;line-height:25px}

.services-bg{left:0;top:849px;width:947px;height:351px;background:linear-gradient(#fbfbfb,#e9e9ea)}
.services-head{left:51px;top:866px;width:848px;display:flex;align-items:center;gap:14px;color:#444;font-size:14px;font-weight:500}
.services-head::before,.services-head::after{content:"";flex:1;height:3px;border-top:1px solid var(--line);border-bottom:1px solid var(--line)}
.card{top:902px;width:201px;height:212px;background:var(--card);box-shadow:0 6px 8px rgba(0,0,0,.12)}
.card h3{height:42px;display:flex;align-items:center;justify-content:center;font-size:14px;font-weight:500;color:#222;border-bottom:1px solid #dcdcdd}
.card .thumb{margin:15px auto 0;width:179px;height:81px;border:1px solid #ccc;background:#fff;padding:2px}
.card .thumb div{width:100%;height:100%}
.card p{margin:15px 12px 0;font-size:11px;line-height:14px;color:#333}
.card .more{margin:4px 12px 0;font-size:9.5px;color:var(--blue);display:flex;align-items:center;gap:3px}

.footer-rule{left:51px;top:1154px;width:848px;height:1px;background:var(--line)}
.copyright{left:51px;top:1172px;font-size:9.5px;color:#333}
.keep{left:651px;top:1170px;font-size:12.5px;font-weight:500;color:#333}
.social{left:760px;top:1164px;display:flex;gap:10px}
.social i{width:24px;height:24px;border-radius:50%;background:#d8d8da;border:1px solid #c4c4c6}
</style>
</head>
<body>

<div class="abs brand"><span class="brand-dot"></span><span class="brand-name">Tovrin SnapStand</span></div>

<nav class="abs nav">
  <a>HOME</a><a>SERVICES</a><a>REVIEWS</a><a>ALBUMGALLERY</a><a>BLOG</a><a>CONTACT</a>
</nav>

<div class="abs band"></div>
<section class="abs slider">
  <div class="abs slide-photo" role="img" aria-label="Fanned collage of photo booth print strips from a party"></div>
  <h2 class="abs slide-title">PLANNING AN EVENT</h2>
  <p class="abs slide-text">The Tovrin SnapStand experience captures the essence of your party with ‘instant prints’ that create a buzz at your event while providing a memorable keepsake for your guests. The digital images allow you to share and create masterpieces with hish-res digital prints. Our rained photo booh hosts are onsite the entire timne to make sure you have a worry free event.</p>
  <a class="abs know-more">KNOW MORE
    <svg width="20" height="20" viewBox="0 0 20 20"><circle cx="10" cy="10" r="8.5" fill="none" stroke="#fff" stroke-width="2"/><path d="M6 10h7M10 6.5l3.5 3.5-3.5 3.5" fill="none" stroke="#fff" stroke-width="2"/></svg>
  </a>
  <div class="abs dots"><i></i><i></i><i></i><i></i><i></i><i></i></div>
</section>

<section class="abs welcome">
  <h1>welcome to <span>TOVRIN SNAPSTAND</span></h1>
  <p>The Tovrin SnapStand experience captures the essence of your party with ‘instant prints’ that create a buzz at your event while providing a memorable keepsake for your guests. The digital images allow you to share and create masterpieces with hish-res digital prints. Our rained photo booh hosts are onsite the entire timne to make sure you have a worry free event.</p>
  <h2>We are perfect for:</h2>
  <p class="events">Weddings, Corporate Events, Holiday &nbsp;Parties, Proms, Graduations, Anniversary &amp; Birthday Parties, Bar/bar Mitzvah’s, Trade Shows, Charity Functions</p>
</section>

<section class="abs media-box">
  <div class="media-inner">
    <div class="abs media-tile" style="left:21px">
      <svg width="112" height="112" viewBox="0 0 112 112"><rect x="2" y="2" width="108" height="108" rx="8" fill="#8aa0d4" stroke="#cdd6ee" stroke-width="2"/><circle cx="56" cy="26" r="13" fill="#3a3a3a"/><path d="M52 20l10 6-10 6z" fill="#fff"/></svg>
    </div>
    <div class="abs media-tile" style="left:281px">
      <svg width="100" height="100" viewBox="0 0 100 100"><rect x="2" y="2" width="96" height="96" rx="14" fill="#f4f4f4"/></svg>
    </div>
    <div class="abs media-cap" style="left:21px">LEARN MORE ABOUT<br>OUR PHOTOBOOTH</div>
    <div class="abs media-cap" style="left:281px">SEE US IN<br>ACTION!</div>
  </div>
</section>

<div class="abs services-bg"></div>
<div class="abs services-head">OUR SERVICES</div>

<article class="abs card" style="left:51px">
  <h3>UNLIMITED PRINTS</h3>
  <div class="thumb"><div role="img" aria-label="Scattered party photo prints" style="background:linear-gradient(120deg,#e6d0c0,#6b3b2a 50%,#2a1f1c)"></div></div>
  <p>All of our Photo Booth Service include....</p>
  <div class="more">Read More <svg width="26" height="6"><path d="M0 3h20" stroke="#2f5fc4" stroke-dasharray="2 2"/><path d="M21 0l3 3-3 3" fill="none" stroke="#2f5fc4"/></svg></div>
</article>
<article class="abs card" style="left:265px">
  <h3>DIGITAL ALBUMS</h3>
  <div class="thumb"><div role="img" aria-label="Phone with camera illustration" style="background:linear-gradient(90deg,#fff 35%,#c9d3ec 50%,#fff 65%)"></div></div>
  <p>All of our Photo Booth Service include....</p>
  <div class="more">Read More <svg width="26" height="6"><path d="M0 3h20" stroke="#2f5fc4" stroke-dasharray="2 2"/><path d="M21 0l3 3-3 3" fill="none" stroke="#2f5fc4"/></svg></div>
</article>
<article class="abs card" style="left:479px">
  <h3>GUEST BOOK</h3>
  <div class="thumb"><div role="img" aria-label="Blue photo guest book" style="background:linear-gradient(90deg,#fff 25%,#9fb3dc 50%,#fff 75%)"></div></div>
  <p>All of our Photo Booth Service include....</p>
  <div class="more">Read More <svg width="26" height="6"><path d="M0 3h20" stroke="#2f5fc4" stroke-dasharray="2 2"/><path d="M21 0l3 3-3 3" fill="none" stroke="#2f5fc4"/></svg></div>
</article>
<article class="abs card" style="left:698px">
  <h3>CUSTOMIZED HEADERS</h3>
  <div class="thumb"><div role="img" aria-label="Photo strip with custom logo header" style="background:linear-gradient(90deg,#fff 25%,#b89a88 50%,#fff 75%)"></div></div>
  <p>All of our Photo Booth Service include....</p>
  <div class="more">Read More <svg width="26" height="6"><path d="M0 3h20" stroke="#2f5fc4" stroke-dasharray="2 2"/><path d="M21 0l3 3-3 3" fill="none" stroke="#2f5fc4"/></svg></div>
</article>

<div class="abs footer-rule"></div>
<div class="abs copyright">©2012, tovrinsnapstandcom, All Rights Reserved &nbsp;| &nbsp;Terms &amp; Conditions</div>
<div class="abs keep">KEEP IN TOUCH</div>
<div class="abs social"><i></i><i></i><i></i><i></i></div>

</body>
</html>
```